BrookVale Collision Repair Web Site

Create a web site that will inform my potential customers about the services I provide. We are a Automotive Collision repair business that uses the latest state of the art equipment, computerized paint matching highly trained technicians, have over 30 years experience. We work with all all insurance programs. Our Moto is "Fixed Right, The First Time, Every Time". BrookVale, The trusted pick in collision repair.

Target Market(s)

People that have been in a auto collision, needs windshield replaced, people that drive 10 year or newer cars

Industry/Entity Type

Automotive

Coding

Coded - Design and coding required

Number of Pages Required

4 page

Font styles to use
Sans Serif

Requirements
Must have
• Logo, Place for Phone number, I need to be able to put the code in so I can use a tracking phone number
• site needs to be mobile ready or adaptive
• May want to have a photo of a high end car
• here is a web site for example with the pages that I want
• https://www.pondlyautobody.example/online-repair-estimate,
• https://www.pondlyautobody.example/schedule-appointment
• https://www.pondlyautobody.example/collision-repair/auto-body-repair
• https://www.pondlyautobody.example/contact
Nice to have
• Be great if the Car in the log could have the front damaged then have it fix in a animation. Not sure if could be done here

```html
<!DOCTYPE html>
<html lang="en">
<head>
<meta charset="utf-8">
<title>BrookVale Collision Repair</title>
<link rel="stylesheet" href="https://fonts.googleapis.com/css2?family=Oswald:wght@400;500&family=Open+Sans:wght@400;600;700&family=Noto+Serif:wght@400;700&display=swap">
<style>
:root{
  --green:#8cc63f;
  --green-dark:#76ad2c;
  --blue:#1d5ea8;
  --ink:#333;
  --muted:#777;
  --line:#d9d9d9;
  --pale:#f3f3f3;
  --dark:#1d1f22;
  --white:#fff;
}
*{box-sizing:border-box;margin:0;padding:0}
html,body{width:1200px;height:4749px;overflow:hidden}
body{position:relative;background:var(--white);font-family:"Open Sans",Arial,sans-serif;color:var(--ink)}
.abs{position:absolute}

/* header */
.brand{left:79px;top:34px;font-family:"Noto Serif",Georgia,serif;font-size:50px;font-weight:700;color:var(--blue);line-height:1;display:flex;align-items:center;gap:14px}
.brand-dot{width:18px;height:18px;border-radius:50%;background:var(--green)}
.brand-sub{left:111px;top:92px;font-family:"Noto Serif",Georgia,serif;font-size:22px;color:var(--blue);letter-spacing:1px}
.call{left:888px;top:34px;font-size:20px;color:var(--green)}
.phone{left:888px;top:68px;font-size:31px;color:var(--blue)}

/* hero */
.hero-photo{left:0;top:158px;width:1200px;height:681px;background:linear-gradient(100deg,#6b6f73 0%,#9a9c9e 35%,#c8c9ca 60%,#8d9094 100%)}
.hero-shade{left:0;top:158px;width:1200px;height:681px;background:linear-gradient(90deg,rgba(0,0,0,.45),rgba(0,0,0,0) 60%)}
.nav{left:79px;top:158px;width:656px;height:48px;background:var(--green);display:flex;align-items:center;padding-left:22px}
.nav a{color:var(--white);text-decoration:none;font-family:"Noto Serif",Georgia,serif;font-size:16px;padding:0 24px;line-height:48px}
.nav a.on{background:var(--green-dark)}
.hero-title{left:101px;top:410px;font-family:"Oswald",Arial,sans-serif;font-weight:500;font-size:56px;line-height:72px;color:var(--white);letter-spacing:1px}
.btn{display:inline-block;text-align:center;font-family:"Noto Serif",Georgia,serif;font-size:17px;color:var(--white);background:var(--green)}
.hero-book{left:101px;top:578px;width:206px;height:62px;line-height:62px}
.hero-contact{left:316px;top:578px;width:206px;height:62px;line-height:58px;background:transparent;border:2px solid var(--white)}

.appt{left:735px;top:206px;width:389px;height:633px;background:rgba(245,245,245,.95);padding:22px 24px}
.appt h3{font-family:"Noto Serif",Georgia,serif;font-weight:400;font-size:18px;color:var(--blue);text-align:center;margin-bottom:18px}
.field{position:relative;height:38px;border:1px solid var(--line);background:var(--white);margin-bottom:14px;font-size:13px;color:var(--muted);line-height:36px;padding-left:12px}
.field.sel::after{content:"";position:absolute;right:14px;top:15px;border:5px solid transparent;border-top:6px solid #555}
.field.hot{background:var(--green);color:var(--white);border-color:var(--green)}
.field.hot::after{border-top-color:var(--white)}
.field.area{height:82px;line-height:20px;padding-top:8px}
.q{font-size:13px;color:#555;margin:2px 0 6px}
.radios{display:flex;gap:20px;font-size:13px;color:#555;margin-left:120px;align-items:center}
.radio{display:inline-flex;align-items:center;gap:6px}
.radio i{width:13px;height:13px;border-radius:50%;border:1px solid #666;display:inline-block;position:relative}
.radio i.on::after{content:"";position:absolute;left:3px;top:3px;width:5px;height:5px;border-radius:50%;background:#333}
.appt .go{display:block;margin:10px auto 0;width:218px;height:48px;line-height:48px}

/* welcome */
.center{left:0;width:1200px;text-align:center}
.welcome-kicker{top:902px;font-family:"Noto Serif",Georgia,serif;font-size:20px;color:var(--ink);letter-spacing:1px}
.welcome-brand{top:934px;font-family:"Noto Serif",Georgia,serif;font-size:50px;font-weight:700;color:var(--blue);line-height:58px}
.welcome-sub{top:992px;font-family:"Noto Serif",Georgia,serif;font-size:22px;color:var(--blue)}
.welcome-text{left:158px;top:1026px;width:884px;text-align:center;font-size:13px;line-height:21px;color:var(--muted)}
.read-more{left:516px;top:1235px;width:168px;height:62px;line-height:62px}

.sec-title{font-family:"Noto Serif",Georgia,serif;font-size:40px;line-height:1;display:flex;align-items:center;justify-content:center;gap:22px}
.sec-title .rule{width:88px;height:2px;background:var(--blue)}
.blue{color:var(--blue)}
.green{color:var(--green)}
.sec-sub{font-size:13.5px;line-height:22px;color:#555}

/* services */
.svc-panel{left:0;top:1488px;width:601px;height:421px;background:#efefef}
.svc-title{left:79px;top:1555px;font-family:"Noto Serif",Georgia,serif;font-weight:400;font-size:40px}
.svc-kicker{left:79px;top:1620px;font-family:"Noto Serif",Georgia,serif;font-size:17px;color:#333}
.svc-text{left:79px;top:1660px;width:440px;font-size:13.5px;line-height:22px;color:#555}
.svc-btn{left:79px;top:1785px;width:202px;height:62px;line-height:62px}
.svc-photo{left:601px;top:1488px;width:599px;height:421px;background:linear-gradient(120deg,#20262e 0%,#3c4450 45%,#6d7480 75%,#2a2f36 100%)}
.svc-icon{left:567px;top:1676px;width:68px;height:68px}
.pager-prev{left:415px;top:1931px;width:171px;height:52px;line-height:48px;color:var(--green);border:2px solid var(--green);background:var(--white);font-size:16px}
.pager-next{left:608px;top:1931px;width:174px;height:52px;line-height:52px;font-size:16px}

/* cards */
.card{top:2137px;width:333px;height:465px;border:1px solid var(--line);background:var(--white)}
.card-photo{height:222px}
.card h4{font-family:"Noto Serif",Georgia,serif;font-weight:400;font-size:17px;color:#333;margin:28px 20px 12px}
.card p{font-size:13.5px;line-height:22px;color:#555;margin:0 20px}
.card .row{position:absolute;left:20px;bottom:22px;display:flex;align-items:center;gap:22px}
.card .row .btn{width:164px;height:48px;line-height:48px;font-size:16px}
.card .row .btn.dark{background:#555}
.price{font-family:"Noto Serif",Georgia,serif;font-size:32px;color:#555}
.price.g{color:var(--green)}

/* estimate */
.est-bg{left:0;top:2669px;width:1200px;height:538px;background:linear-gradient(180deg,#2a2c2f,#17181a)}
.est-title{top:2728px;color:var(--white)}
.est-title .rule{background:var(--white)}
.est-form{left:117px;top:2820px;width:968px}
.grid{display:grid;gap:16px}
.est-form .field{height:40px;border:1px solid var(--white);background:transparent;color:var(--white);margin:0}
.est-form .field.sel::after{border-top-color:var(--white)}
.est-form .field.hot{background:var(--green);border-color:var(--green)}
.est-form .radios{color:var(--white)}
.est-form .radio i{border-color:var(--white)}
.est-form .radio i.on::after{background:var(--white)}
.est-go{left:117px;top:3096px;width:968px;height:50px;line-height:50px;background:var(--white);color:var(--green)}

/* guarantee */
.guar{left:0;top:3213px;width:1200px;height:396px;background:var(--green)}
.guar-title{left:378px;top:3276px;color:var(--white)}
.guar-title .rule{background:var(--white)}
.guar-text{left:434px;top:3370px;width:660px;font-family:"Noto Serif",Georgia,serif;font-size:19px;line-height:32px;color:var(--white)}
.guar-btn{left:434px;top:3476px;width:174px;height:64px;line-height:64px;background:var(--white);color:var(--green)}
.seal{left:142px;top:3277px;width:270px;height:270px;border-radius:50%;background:radial-gradient(circle,#f3d77a,#c9962a 70%,#8a6614)}

/* testimonials */
.clients{left:0;top:3609px;width:1200px;height:459px;background:linear-gradient(180deg,#f4f4f4,#fafafa)}
.client-title{top:3670px}
.quote{left:218px;top:3740px;width:764px;text-align:center;font-size:14px;line-height:24px;color:#555}
.avatar{left:553px;top:3829px;width:94px;height:94px;border-radius:50%;background:radial-gradient(circle at 50% 40%,#c9b29a,#6d7a66);border:4px solid var(--white);box-shadow:0 0 0 1px var(--line)}
.client-name{top:3947px;font-size:12px;color:var(--blue)}
.dots{display:flex;gap:8px;justify-content:center}
.dots i{width:12px;height:12px;transform:rotate(45deg);border:2px solid var(--blue);display:block}
.dots i.on{background:var(--blue)}

/* partners */
.partner{top:4131px;width:174px;height:143px;background:var(--white);border:1px solid #eee;display:flex;align-items:center;justify-content:center}
.partner span{width:96px;height:96px;border-radius:50%;background:#d6d6d6}
.partner span.sq{border-radius:10px;width:110px;height:70px}

/* footer */
.foot{left:0;top:4369px;width:1200px;height:380px;background:linear-gradient(180deg,#26282b,#111214)}
.foot-brand{top:4425px;font-family:"Noto Serif",Georgia,serif;font-size:50px;font-weight:700;color:var(--blue);line-height:58px}
.foot-sub{top:4484px;font-family:"Noto Serif",Georgia,serif;font-size:22px;color:var(--blue)}
.socials{left:0;top:4575px;width:1200px;display:flex;justify-content:center;gap:34px}
.socials i{width:44px;height:44px;background:var(--green);transform:rotate(45deg);display:block}
.copy{top:4680px;font-size:13px;color:#ccc}
.copy b{color:var(--green);font-weight:400}
</style>
</head>
<body>

<header>
  <div class="abs brand">BrookVale<span class="brand-dot"></span></div>
  <div class="abs brand-sub">Collision Repair</div>
  <div class="abs call">CALL US NOW :</div>
  <div class="abs phone">+(00)0123 456 789</div>
</header>

<section class="hero">
  <div class="abs hero-photo" role="img" aria-label="Technician in a cap working in a collision repair workshop"></div>
  <div class="abs hero-shade"></div>
  <nav class="abs nav">
    <a class="on" href="#">HOME</a><a href="#">ABOUT</a><a href="#">SERVICES</a><a href="#">APPOINTMENT</a><a href="#">CONTACT</a>
  </nav>
  <h1 class="abs hero-title">THE INTELLIGENT CHOICE<br>IN COLLISION REPAIR.</h1>
  <a class="abs btn hero-book">BOOK NOW</a>
  <a class="abs btn hero-contact">CONTACT US</a>

  <form class="abs appt">
    <h3>SCHEDULE APPOINTMENT</h3>
    <div class="field sel hot">Services*</div>
    <div class="field sel">Year*</div>
    <div class="field sel">Make*</div>
    <div class="field sel">Model*</div>
    <div class="field sel">Body Style*</div>
    <div class="field sel">Type of Service</div>
    <div class="field area">Description of  Damage*</div>
    <p class="q">Will an insurance claim be submitted for damages?</p>
    <div class="radios"><span class="radio"><i class="on"></i>Yes</span><span class="radio"><i></i>No</span></div>
    <a class="btn go">CONTINUE</a>
  </form>
</section>

<section class="welcome">
  <div class="abs center welcome-kicker">WEL COME TO</div>
  <div class="abs center welcome-brand">BrookVale</div>
  <div class="abs center welcome-sub">Collision Repair</div>
  <p class="abs welcome-text">Lorem Ipsum is simply dummy text of the printing and typesetting industry. Lorem Ipsum has been the industry's standard dummy text ever since the 1500s, when an unknown printer took a galley of type and scrambled it to make a type specimen book. It has survived not only five centuries, but also the leap into electronic typesetting, remaining essentially unchanged. It was popularised in the 1960s with the release of Typemark sheets containing Lorem Ipsum passages, and more recently with desktop publishing software like Pagewright Studio including versions of Lorem Ipsum. It is a long established fact that a reader will be distracted by the readable content of a page when looking at its layout. The point of using Lorem Ipsum is that it has a more-or-less normal distribution of letters, as opposed to using 'Content here, content here', making it look like readable English.</p>
  <a class="abs btn read-more">READ MORE</a>
</section>

<section class="services">
  <h2 class="abs center sec-title" style="top:1352px"><span class="rule"></span><span><span class="blue">OUR</span> <span class="green">SERVICES</span></span><span class="rule"></span></h2>
  <p class="abs center sec-sub" style="top:1410px">Lorem Ipsum is simply dummy text of the printing and typesetting industry. Lorem Ipsum has been the industry's<br>standard dummy text ever since the 1500s</p>

  <div class="abs svc-panel"></div>
  <h3 class="abs svc-title"><span class="green">AUTO</span> <span class="blue">BODY REPAIR</span></h3>
  <div class="abs svc-kicker">FENDER REPAIR</div>
  <p class="abs svc-text">Lorem Ipsum is simply dummy text of the printing and typesetting industry. Lorem Ipsum has been the industry's standard dummy text ever since the 1500s, when an unknown printer took a galley of type and scrambled it to make a type specimen book. It has survived not only five centuries, but also the leap into electronic typesetting, ...</p>
  <a class="abs btn svc-btn">CONTACT US</a>
  <div class="abs svc-photo" role="img" aria-label="Two technicians repairing the front of a dark blue car"></div>
  <svg class="abs svc-icon" viewBox="0 0 68 68" aria-hidden="true">
    <circle cx="34" cy="34" r="32" fill="#8cc63f" stroke="#fff" stroke-width="4"/>
    <circle cx="28" cy="38" r="8" fill="none" stroke="#fff" stroke-width="4"/>
    <circle cx="42" cy="26" r="5" fill="none" stroke="#fff" stroke-width="3"/>
  </svg>
  <a class="abs btn pager-prev">PREVIOUS</a>
  <a class="abs btn pager-next">NEXT</a>
</section>

<section class="what">
  <h2 class="abs center sec-title" style="top:2048px"><span class="rule"></span><span><span class="blue">WHAT</span> <span class="green">WE DO</span></span><span class="rule"></span></h2>

  <article class="abs card" style="left:79px">
    <div class="card-photo" role="img" aria-label="Pink sports car in a showroom" style="background:linear-gradient(135deg,#2a1830,#b0447e 50%,#3a2234)"></div>
    <h4>ART EQUIPMENT</h4>
    <p>Lorem Ipsum is simply dummy text of the printing and typesetting. Lorem Ipsum has been the industry's...</p>
    <div class="row"><a class="btn">CONTACT US</a><span class="price g">$ 80.58</span></div>
  </article>
  <article class="abs card" style="left:434px">
    <div class="card-photo" role="img" aria-label="Freshly painted pink supercar" style="background:linear-gradient(135deg,#1d1d24,#e05fbf 50%,#2a2430)"></div>
    <h4>COMPUTERIZED PAINT</h4>
    <p>Lorem Ipsum is simply dummy text of the printing and typesetting. Lorem Ipsum has been the industry's...</p>
    <div class="row"><a class="btn dark">CONTACT US</a><span class="price">$ 80.58</span></div>
  </article>
  <article class="abs card" style="left:788px">
    <div class="card-photo" role="img" aria-label="Technician working on a car engine" style="background:linear-gradient(135deg,#3d4a5a,#8a96a4 50%,#4a4f56)"></div>
    <h4>HIGHLY TRAINED  TECHNICIANS</h4>
    <p>Lorem Ipsum is simply dummy text of the printing and typesetting. Lorem Ipsum has been the industry's...</p>
    <div class="row"><a class="btn dark">CONTACT US</a><span class="price">$ 80.58</span></div>
  </article>
</section>

<section class="estimate">
  <div class="abs est-bg" role="img" aria-label="Dimmed workshop background"></div>
  <h2 class="abs center sec-title est-title"><span class="rule"></span><span>ONLINE <span class="green">REPAIR ASTIMET</span></span><span class="rule"></span></h2>
  <form class="abs est-form">
    <div class="grid" style="grid-template-columns:1fr 1fr 1fr">
      <div class="field sel hot">Services*</div><div class="field sel">Year*</div><div class="field sel">Make*</div>
      <div class="field sel">Model*</div><div class="field sel">Body Style*</div><div class="field sel">VIN</div>
    </div>
    <div class="grid" style="grid-template-columns:1fr 2fr;margin-top:16px">
      <div>
        <div class="field sel">Type of Service</div>
        <div class="field" style="height:96px;margin-top:10px;line-height:22px;padding-top:8px">Will an insurance claim be submitted for damages?<div class="radios" style="margin:6px 0 0"><span class="radio"><i class="on"></i>Yes</span><span class="radio"><i></i>No</span></div></div>
      </div>
      <div class="field" style="height:146px;line-height:22px;padding-top:8px">Description of  Damage*</div>
    </div>
  </form>
  <a class="abs btn est-go">CONTINUE</a>
</section>

<section class="guarantee">
  <div class="abs guar"></div>
  <h2 class="abs sec-title guar-title"><span class="rule"></span><span>LIFETIME  GUARANTEE</span><span class="rule"></span></h2>
  <div class="abs seal" role="img" aria-label="Gold satisfaction guaranteed seal"></div>
  <p class="abs guar-text">We proudly stand behind our repair work for as long as you own your vehicle. Learn more about our Lifetime Guarantee.</p>
  <a class="abs btn guar-btn">GUARANTEE</a>
</section>

<section class="testimonials">
  <div class="abs clients"></div>
  <h2 class="abs center sec-title client-title"><span class="rule"></span><span><span class="blue">WHAT</span> <span class="green">OUR CLIENT SAY</span></span><span class="rule"></span></h2>
  <p class="abs quote">" Lorem Ipsum is simply dummy text of the printing and typesetting industry. Lorem Ipsum has been the industry's standard dummy text ever since the. Lorem Ipsum is simple dummy text "</p>
  <div class="abs avatar" role="img" aria-label="Client portrait"></div>
  <div class="abs center client-name">CLIENT NAME</div>
  <div class="abs center dots" style="top:3990px"><i></i><i class="on"></i><i></i></div>
</section>

<section class="partners">
  <div class="abs partner" style="left:79px"><span></span></div>
  <div class="abs partner" style="left:294px"><span class="sq"></span></div>
  <div class="abs partner" style="left:510px"><span></span></div>
  <div class="abs partner" style="left:725px"><span class="sq"></span></div>
  <div class="abs partner" style="left:940px"><span></span></div>
  <div class="abs center dots" style="top:4292px"><i></i><i class="on"></i><i></i></div>
</section>

<footer>
  <div class="abs foot" role="img" aria-label="Dimmed garage background"></div>
  <div class="abs center foot-brand">BrookVale</div>
  <div class="abs center foot-sub">Collision Repair</div>
  <div class="abs socials"><i></i><i></i><i></i></div>
  <div class="abs center copy">© <b>BROOKVALE COLLISION REPAIR</b> - 2016, All rights reserved.</div>
</footer>

</body>
</html>
```